Mother's Day Sale Banner Ad For Jewelry Site

We are looking for a designer to design a banner on our website advertising our Mother's Day Sale. I have enclosed a few pieces of jewelry we would like used in the ad. The ad size needs to be 1187 × 400. The ad should say:

Mother's Day Sale - Save 15% with Promo Code: LOVEMOM

Industry/Entity Type

Jewelry

```html
<!DOCTYPE html>
<html lang="en">
<head>
<meta charset="utf-8">
<title>Mother's Day Sale Banner</title>
<link rel="stylesheet" href="https://fonts.googleapis.com/css2?family=Montserrat:wght@600&family=Open+Sans:wght@400;600&family=Prata&family=Italianno&display=swap">
<style>
  :root {
    --stage: #dcdcdc;
    --banner-bg: #f6f6f6;
    --ribbon: #2b2b2b;
    --gold: #f2b544;
    --gold-deep: #c38a2a;
    --ink: #222222;
    --ink-soft: #3a3a3a;
    --rule: #8a8a8a;
  }
  * { margin: 0; padding: 0; box-sizing: border-box; }
  html, body {
    width: 1200px;
    height: 519px;
    overflow: hidden;
  }
  body {
    background: var(--stage);
    position: relative;
  }
  .banner {
    position: absolute;
    left: 47px;
    top: 54px;
    width: 1100px;
    height: 370px;
    background: linear-gradient(90deg, #fbfbfb 0%, var(--banner-bg) 50%, #f1f1f1 100%);
    overflow: hidden;
  }
  .hero-photo {
    position: absolute;
    left: 0;
    top: 0;
    width: 360px;
    height: 370px;
    background:
      linear-gradient(90deg, rgba(246,246,246,0) 65%, var(--banner-bg) 100%),
      linear-gradient(160deg, #e9c98f 0%, #d8ab7c 35%, #c9926b 55%, #efe6dc 85%);
  }
  .jewelry-photo {
    position: absolute;
    left: 815px;
    top: 17px;
    width: 270px;
    height: 327px;
    border-radius: 6px;
    background:
      radial-gradient(circle at 30% 15%, #e0c98c 0%, rgba(224,201,140,0) 28%),
      radial-gradient(circle at 85% 20%, #e89a7c 0%, rgba(232,154,124,0) 16%),
      radial-gradient(circle at 55% 50%, #d5ad5a 0%, rgba(213,173,90,0) 38%),
      radial-gradient(circle at 22% 85%, #3fb3c6 0%, rgba(63,179,198,0) 15%),
      radial-gradient(circle at 80% 85%, #c9617e 0%, rgba(201,97,126,0) 15%),
      var(--banner-bg);
  }
  .offer {
    position: absolute;
    left: 377px;
    top: 0;
    width: 396px;
    height: 370px;
    text-align: center;
  }
  .offer__ribbon {
    position: absolute;
    left: 0;
    top: 29px;
    width: 396px;
    height: 48px;
  }
  .offer__title {
    position: absolute;
    left: 0;
    top: 29px;
    width: 396px;
    line-height: 48px;
    font-family: "Montserrat", sans-serif;
    font-weight: 600;
    font-size: 27px;
    letter-spacing: 0.5px;
    color: var(--gold);
  }
  .offer__eyebrow {
    position: absolute;
    left: 0;
    top: 91px;
    width: 390px;
    height: 18px;
    line-height: 18px;
    display: flex;
    align-items: center;
    gap: 14px;
    font-family: "Open Sans", sans-serif;
    font-weight: 600;
    font-size: 13px;
    color: var(--gold-deep);
  }
  .offer__eyebrow::before,
  .offer__eyebrow::after {
    content: "";
    flex: 1;
    height: 1px;
    background: var(--rule);
  }
  .offer__amount {
    position: absolute;
    left: 0;
    top: 120px;
    width: 390px;
    font-family: "Prata", serif;
    font-size: 134px;
    line-height: 1;
    color: var(--ink);
  }
  .offer__rule {
    position: absolute;
    left: 0;
    width: 390px;
    height: 1px;
    background: var(--rule);
  }
  .offer__rule--upper { top: 251px; }
  .offer__rule--lower { top: 303px; }
  .offer__label {
    position: absolute;
    left: 0;
    top: 262px;
    width: 390px;
    font-family: "Open Sans", sans-serif;
    font-size: 21px;
    line-height: 28px;
    color: var(--ink-soft);
  }
  .offer__code {
    position: absolute;
    left: 0;
    top: 309px;
    width: 390px;
    font-family: "Italianno", cursive;
    font-size: 46px;
    line-height: 46px;
    color: var(--gold-deep);
  }
</style>
</head>
<body>
  <section class="banner" aria-label="Mother's Day Sale banner">
    <div class="hero-photo" role="img" aria-label="Photograph of a smiling mother and daughter embracing in sunlight"></div>

    <div class="offer">
      <svg class="offer__ribbon" viewBox="0 0 396 48" aria-hidden="true">
        <polygon points="0,0 396,0 384,24 396,48 0,48 12,24" fill="var(--ribbon)"/>
      </svg>
      <h1 class="offer__title">MOTHER'S DAY SALE</h1>
      <p class="offer__eyebrow">SAVE UPTO</p>
      <p class="offer__amount">15%</p>
      <div class="offer__rule offer__rule--upper"></div>
      <p class="offer__label">WITH PROMO CODE:</p>
      <div class="offer__rule offer__rule--lower"></div>
      <p class="offer__code">Love Mom</p>
    </div>

    <div class="jewelry-photo" role="img" aria-label="Photographs of jewelry pieces: a gold and diamond band, a coral ring, gold and diamond earrings, turquoise earrings and a jeweled crab brooch"></div>
  </section>
</body>
</html>
```